Creation of Brelto Promo remarketing banners / Creation of Brelto Promo remarketing banners

Hello!
Name: Korvi Media
Website: https://korvimedia.ca/
Activity sector: Website creation
Project: Creation of web banners
Description:
We are a web marketing agency specializing in website design. For a Brelto Promo remarketing campaign, we need:
- 6 banners each with a different background and different text in 300 x 250 px format (300 wide and 250 high).
On the design side, we want the banner to be:
- Simple and refined
- In the colors of our company: green, blue and gray (see our website)
- With a background image that represents the website design (a computer, a tablet, a cell phone, etc.)
For the design, we must take the example of the PageLoom model (attached file).
On the writing side, each banner must have a sentence and a call to action (different clickable button).
Example: In the Tundrel model, first image at the top left), there is the phrase “Be fast, flexible, secure. "And the call to action" Upgrade your Tundrel ".
Here are the 6 different texts to put on the banners (sentence + call to action):
1) Phrase: "Your phone should ring now"
Call to action: "Get a website"
2) Phrase: "One click away from success"
3) Phrase: "Boost your income online"
4) Phrase: "Win new customers"
5) Phrase: "Be where your customers are looking for you"
6) Phrase: "Increase your turnover"
On the font side, it would be good to take the example of the Tundrel banners (attached file) by putting words in front with a larger font (vary the sizes of the words of the same sentence to put the emphasis).
Thank you!
VERSION FRANCAISE
Hello!
Company name: Korvi Media
Sector of activity: Website creation
Description:
We are a web marketing agency specialized in website creation. For a Brelto Promo remarketing campaign, we need:
- 6 banners each with a different background and a different text in 300 x 250 px format (300 width and 250 height).
- Simple and uncluttered
- With a background image that represents the design of a website (a computer, tablet, mobile, etc.).
For the design, we must take the PageLoom template (in attachment) as an example.
Example: In the Tundrel template, first image on the top left), there is the sentence "Be fast, flexible, secure." And the call to action "Upgrade your Tundrel".
1) Sentence: "Your phone must ring now"
2) Sentence: "One click away from success"
3) Sentence: "Boost your income online"
4) Award: "Win new customers"
5) Sentence: "Be where your customers are looking for you"
6) Sentence: "Increase your turnover"
On the font side, it would be good to take the Tundrel banner model (in attachment) as an example by highlighting words with a larger font (vary the size of words in the same sentence to put the emphasis).
Thank you!

```html
<!DOCTYPE html>
<html lang="en">
<head>
<meta charset="utf-8">
<title>Korvi Media – Brelto Promo remarketing banners</title>
<link href="https://fonts.googleapis.com/css2?family=Oswald:wght@300;400&display=swap" rel="stylesheet">
<style>
  :root {
    --green: #8cc152;
    --green-dark: #3f7f22;
    --green-pale: #e8f2dc;
    --blue: #2fa3d6;
    --blue-light: #6cc0e6;
    --teal-blue: #2a93b2;
    --navy: #1f5f8f;
    --turquoise: #1cc1b5;
    --ink: #111111;
    --white: #ffffff;
    --page: #ffffff;
  }
  * { margin: 0; padding: 0; box-sizing: border-box; }
  html, body { width: 1200px; height: 742px; overflow: hidden; background: var(--page); }
  .sheet { position: relative; width: 1200px; height: 742px; }
  .banner {
    position: absolute; width: 300px; height: 250px; overflow: hidden;
    transform: scale(1.1733); transform-origin: 0 0;
    box-shadow: 0 1px 5px rgba(0,0,0,.22);
    font-family: "Oswald", "Arial Narrow", sans-serif; font-weight: 300;
    text-transform: uppercase; letter-spacing: -0.2px;
  }
  .banner svg.shapes, .banner .visual { position: absolute; left: 0; top: 0; width: 300px; height: 250px; }
  .headline, .cta { position: absolute; }
  .cta {
    display: flex; align-items: center; justify-content: center;
    border: 2px solid currentColor; font-size: 16px; white-space: nowrap;
  }
  .pos-1 { left: 42px; top: 57px; }
  .pos-2 { left: 417px; top: 57px; }
  .pos-3 { left: 816px; top: 57px; }
  .pos-4 { left: 42px; top: 397px; }
  .pos-5 { left: 417px; top: 397px; }
  .pos-6 { left: 816px; top: 397px; }

  /* 1 – phone */
  .banner-phone { background: var(--white); color: var(--ink); }
  .banner-phone .headline { left: 150px; top: 24px; font-size: 24px; line-height: 32px; }
  .banner-phone .cta { left: 159px; top: 148px; width: 118px; height: 53px; font-size: 17px; }

  /* 2 – click */
  .banner-click { color: var(--white); }
  .banner-click .headline { left: 12px; top: 12px; font-size: 22px; line-height: 30px; }
  .banner-click .cta { left: 14px; top: 86px; width: 106px; height: 48px; }

  /* 3 – income */
  .banner-income { background: var(--teal-blue); color: var(--white); }
  .banner-income .headline { left: 0; width: 300px; top: 12px; text-align: center; font-size: 22px; line-height: 30px; }
  .banner-income .cta { left: 185px; top: 170px; width: 106px; height: 48px; }

  /* 4 – customers looking */
  .banner-looking { color: var(--white); }
  .banner-looking .headline { left: 0; width: 300px; top: 125px; text-align: center; font-size: 20px; line-height: 28px; }
  .banner-looking .cta { left: 100px; top: 193px; width: 100px; height: 45px; }

  /* 5 – win */
  .banner-win { background: var(--blue); color: var(--white); }
  .banner-win .headline { left: 0; width: 300px; top: 4px; text-align: center; font-size: 22px; line-height: 30px; }
  .banner-win .cta { left: 97px; top: 192px; width: 106px; height: 47px; background: rgba(20,30,40,.55); }

  /* 6 – turnover */
  .banner-turnover { background: var(--white); color: var(--ink); }
  .banner-turnover .headline { left: 104px; top: 16px; font-size: 24px; line-height: 32px; }
  .banner-turnover .headline .indent { display: block; padding-left: 64px; }
  .banner-turnover .cta { left: 187px; top: 94px; width: 102px; height: 45px; border: none; background: var(--green); color: var(--white); }
</style>
</head>
<body>
<main class="sheet">

  <!-- 1 -->
  <section class="banner banner-phone pos-1">
    <svg class="shapes" viewBox="0 0 300 250" aria-hidden="true">
      <polygon points="95,0 150,0 150,140 112,250 60,250" fill="var(--green-pale)"/>
      <polygon points="100,0 140,0 150,140 128,48" fill="var(--green)"/>
      <polygon points="0,0 18,0 131,46 136,168 96,250 0,250" fill="var(--blue-light)"/>
    </svg>
    <svg class="visual" viewBox="0 0 300 250" role="img" aria-label="Photo of a smartphone showing the Korvi Media name, lying on a white blanket beside a plant">
      <defs>
        <linearGradient id="phonePhoto" x1="0" y1="0" x2="1" y2="1">
          <stop offset="0" stop-color="#d9d4cc"/>
          <stop offset="1" stop-color="#a9a79b"/>
        </linearGradient>
      </defs>
      <polygon points="0,0 12,0 124,52 128,164 88,250 0,250" fill="url(#phonePhoto)"/>
    </svg>
    <p class="headline">"Your phone<br>should ring<br>now"</p>
    <span class="cta">Get a website</span>
  </section>

  <!-- 2 -->
  <section class="banner banner-click pos-2">
    <div class="visual" role="img" aria-label="Photo of a keyboard with a bright green click key pressed by a finger" style="background: linear-gradient(135deg, #6d7a68 0%, #8c9a84 45%, #9fcf3a 75%, #c8d6b8 100%);"></div>
    <svg class="shapes" viewBox="0 0 300 250" aria-hidden="true">
      <polygon points="0,0 300,0 300,20 0,250" fill="rgba(40,40,40,.45)"/>
      <polygon points="300,20 300,250 175,250" fill="rgba(140,193,82,.35)"/>
    </svg>
    <p class="headline">"One click away from<br>success"</p>
    <span class="cta">Get a website</span>
  </section>

  <!-- 3 -->
  <section class="banner banner-income pos-3">
    <svg class="shapes" viewBox="0 0 300 250" aria-hidden="true">
      <polygon points="215,90 300,35 300,120" fill="var(--green-dark)"/>
      <polygon points="180,165 300,55 300,250 170,250" fill="var(--green)"/>
      <polygon points="180,165 210,150 200,250 170,250" fill="var(--green-dark)"/>
    </svg>
    <div class="visual" role="img" aria-label="Illustration of a laptop with a magnet attracting gold coins" style="left:10px; top:60px; width:160px; height:170px; background: linear-gradient(160deg, rgba(244,193,70,.55) 0%, rgba(240,246,250,.85) 55%, rgba(210,226,236,.9) 100%); border-radius: 6px;"></div>
    <p class="headline">"Boost your income online"</p>
    <span class="cta">Get a website</span>
  </section>

  <!-- 4 -->
  <section class="banner banner-looking pos-4">
    <div class="visual" role="img" aria-label="Photo of a cheerful woman celebrating while holding a phone at home" style="background: linear-gradient(120deg, #6d6257 0%, #b9a695 45%, #8e857c 100%);"></div>
    <svg class="shapes" viewBox="0 0 300 250" aria-hidden="true">
      <rect x="0" y="100" width="300" height="150" fill="rgba(20,20,20,.55)"/>
      <polygon points="0,250 300,105 300,250" fill="rgba(47,163,214,.85)"/>
      <polygon points="150,250 300,120 300,250" fill="rgba(140,193,82,.9)"/>
    </svg>
    <p class="headline">"Be where your customers are<br>looking for you"</p>
    <span class="cta">Get a website</span>
  </section>

  <!-- 5 -->
  <section class="banner banner-win pos-5">
    <svg class="shapes" viewBox="0 0 300 250" aria-hidden="true">
      <polygon points="0,0 300,0 300,30 0,52" fill="var(--green)"/>
      <polygon points="0,52 300,30 300,40 0,62" fill="#1f8fc4"/>
    </svg>
    <div class="visual" role="img" aria-label="Photo of a smiling man looking at his smartphone" style="left:70px; top:50px; width:160px; height:200px; background: linear-gradient(180deg, #4a3a30 0%, #7a5a45 45%, #8c8c8c 75%, #a5a5a5 100%); border-radius: 70px 70px 0 0;"></div>
    <p class="headline">"Win new customers"</p>
    <span class="cta">Get a website</span>
  </section>

  <!-- 6 -->
  <section class="banner banner-turnover pos-6">
    <svg class="shapes" viewBox="0 0 300 250" aria-hidden="true">
      <circle cx="22" cy="30" r="15" fill="#2aa84a"/>
      <text x="22" y="37" text-anchor="middle" font-family="Oswald, sans-serif" font-size="19" fill="#fff">$</text>
      <path d="M37 30 H48 V8" fill="none" stroke="#222" stroke-width="2.5"/>
      <polygon points="42,10 48,2 54,10" fill="#222"/>
      <polygon points="0,75 135,82 160,95 0,88" fill="var(--navy)"/>
      <polygon points="0,88 160,95 300,215 300,250 0,250" fill="var(--turquoise)"/>
      <polygon points="160,95 195,115 300,200 300,250 280,250" fill="var(--green-dark)"/>
      <polygon points="160,95 300,215 300,235" fill="var(--turquoise)"/>
    </svg>
    <div class="visual" role="img" aria-label="Illustration of a money bag, banknotes, coins, a calculator and a rising chart" style="left:15px; top:135px; width:175px; height:100px; background: linear-gradient(180deg, rgba(255,255,255,.35) 0%, rgba(60,70,80,.55) 55%, rgba(140,193,82,.6) 100%); border-radius: 6px;"></div>
    <p class="headline">"Increase your<span class="indent">turnover"</span></p>
    <span class="cta">Get a website</span>
  </section>

</main>
</body>
</html>
```